Agricultural Consulting Website

Provide a modern yet business like website for my new Agriculture Consulting Business in Australia called FenTrove. Whilst we are based in Australia we are targetting both domestic and international markets (especially in Asia). We are targetting corporate, small business, government and farmer clients. The design should compliment our logo also sourced through pixel guild. The webiste should be easy for me to keep updated on a regular basis without the need to go back to the designer.

Industry/Entity Type

Business

Requirements
Must have
• clean crisp feel
• be modern yet business like
• be able to be updated by myself easily

```html
<!DOCTYPE html>
<html lang="en">
<head>
<meta charset="utf-8">
<title>FenTrove – Agricultural Consulting</title>
<link rel="stylesheet" href="https://fonts.googleapis.com/css2?family=Open+Sans:wght@400;600&family=Raleway:wght@400;500&display=swap">
<style>
  :root {
    --green: #6a9f16;
    --green-dark: #4f7c0c;
    --green-light: #86b929;
    --brown: #7a3e0c;
    --brown-dark: #5f2f08;
    --text: #333333;
    --muted: #555555;
    --field: #efefef;
    --field-border: #c9c9c9;
    --white: #ffffff;
    --social-a: #2a9fd8;
    --social-b: #3b5fc0;
  }
  * { box-sizing: border-box; margin: 0; padding: 0; }
  html, body { width: 1200px; height: 1037px; overflow: hidden; }
  body {
    position: relative;
    font-family: "Open Sans", Arial, sans-serif;
    color: var(--text);
    background: linear-gradient(to bottom, #3c79c8 0%, #9fbfe0 18%, #5f7d3e 32%, #b97a32 42%, #c88a3e 70%, #8a4e1c 100%);
  }
  .page {
    position: absolute; left: 157px; top: 0; width: 881px; height: 1037px;
    background: var(--white);
  }
  .abs { position: absolute; }

  /* header */
  .brand { left: 28px; top: 29px; display: flex; align-items: center; gap: 8px; }
  .brand-mark { width: 53px; height: 53px; background: var(--brown); }
  .brand-name { font-size: 31px; font-weight: 400; color: var(--green); white-space: nowrap; }
  .social { top: 18px; left: 611px; display: flex; gap: 8px; }
  .social span { width: 28px; height: 28px; border-radius: 50%; display: block; }
  .social span:first-child { background: var(--social-a); }
  .social span:last-child { background: var(--social-b); }
  .divider { left: 689px; top: 24px; width: 1px; height: 15px; background: #bbb; }
  .search {
    left: 705px; top: 18px; width: 150px; height: 28px;
    border: 1px solid var(--field-border); background: #f6f6f6;
    font-size: 11px; color: #555; padding: 6px 8px;
  }
  .search svg { position: absolute; right: 7px; top: 6px; }
  .nav {
    left: 391px; top: 64px; width: 462px;
    display: flex; justify-content: space-between;
    font-size: 12.5px; white-space: nowrap;
  }
  .nav a { color: var(--text); text-decoration: none; }
  .nav a.current { color: var(--green); }
  .header-rule { left: 0; top: 98px; width: 881px; height: 2px; background: #e3e3e3; }

  /* hero */
  .hero {
    left: 28px; top: 99px; width: 828px; height: 311px;
    background: linear-gradient(to bottom, #e9a56e 0%, #f2c79a 30%, #c9a06a 55%, #b58a4e 100%);
  }
  .hero-copy { left: 53px; top: 80px; font-family: "Raleway", sans-serif; color: #4a3220; white-space: nowrap; }
  .hero-copy h1 { font-size: 24.5px; font-weight: 500; margin-bottom: 8px; }
  .hero-copy p { font-size: 17.5px; font-weight: 500; line-height: 22px; }
  .btn-join {
    left: 53px; top: 184px; width: 95px; height: 32px;
    background: linear-gradient(#8f4c14, var(--brown-dark)); border-radius: 3px;
    color: var(--white); font-family: "Raleway", sans-serif; font-size: 13px;
    display: flex; align-items: center; justify-content: center; gap: 5px;
  }
  .slider-dots {
    left: 390px; top: 398px; width: 107px; height: 31px; border-radius: 16px;
    background: linear-gradient(#ffffff, #ececec); box-shadow: 0 3px 6px rgba(0,0,0,.2);
    display: flex; align-items: center; justify-content: center; gap: 9px;
  }
  .slider-dots span { width: 14px; height: 14px; border-radius: 50%; border: 1px solid #bbb; background: #f4f4f4; }
  .slider-dots span.active { background: #cfcfcf; }

  /* feature columns */
  .feature { top: 463px; width: 246px; }
  .feature-img { width: 246px; height: 126px; border: 1px solid #d6d6d6; }
  h2 { font-size: 17px; font-weight: 400; color: var(--text); line-height: 22px; white-space: nowrap; }
  h2 em { font-style: normal; color: var(--green); }
  .feature h2 { margin-top: 15px; }
  .feature p { margin-top: 9px; font-size: 11.5px; line-height: 16.7px; color: var(--muted); }
  .btn-more {
    display: flex; align-items: center; justify-content: center;
    width: 54px; height: 26px; background: linear-gradient(var(--green-light), var(--green-dark));
    color: var(--white); font-size: 12px; font-weight: 600; border-radius: 2px;
  }
  .feature .btn-more { margin-top: 16px; }

  /* about + subscribe */
  .about { left: 27px; top: 756px; width: 536px; }
  .about-rule { border-top: 1px dashed #cfcfcf; margin-top: 8px; }
  .about p { margin-top: 10px; font-size: 11.5px; line-height: 16.7px; color: var(--muted); text-align: justify; }
  .about .btn-more { margin-top: 18px; }
  .subscribe { left: 611px; top: 756px; width: 244px; }
  .field {
    height: 34px; background: var(--field); border: 1px solid var(--field-border);
    font-size: 11.5px; color: #444; padding: 9px 9px; margin-top: 10px;
  }
  .subscribe .field:first-of-type { margin-top: 9px; }
  .btn-submit {
    margin-top: 12px; width: 76px; height: 34px;
    background: linear-gradient(var(--green-light), var(--green-dark));
    color: var(--white); font-size: 13px; display: flex; align-items: center; justify-content: center;
  }

  /* footer */
  .footer {
    left: 0; top: 967px; width: 881px; height: 70px;
    background: linear-gradient(#6a3408, var(--brown) 40%, #86460f);
    border-top: 2px solid var(--brown-dark);
    color: #f1e2d3; font-size: 11.5px; white-space: nowrap;
  }
  .footer-nav { position: absolute; left: 28px; top: 26px; display: flex; }
  .footer-nav a { color: #f1e2d3; text-decoration: none; margin-right: 21px; }
  .footer-nav a.current { color: var(--white); text-decoration: underline; }
  .copyright { position: absolute; right: 25px; top: 26px; }
</style>
</head>
<body>
<div class="page">
  <header>
    <div class="abs brand"><span class="brand-mark"></span><span class="brand-name">FenTrove</span></div>
    <div class="abs social"><span></span><span></span></div>
    <div class="abs divider"></div>
    <div class="abs search">Search
      <svg width="14" height="14" viewBox="0 0 14 14"><circle cx="8" cy="6" r="4.5" fill="none" stroke="#444" stroke-width="1.5"/><line x1="4.8" y1="9.2" x2="1" y2="13" stroke="#444" stroke-width="1.8"/></svg>
    </div>
    <nav class="abs nav">
      <a class="current" href="#">Home</a><a href="#">About Us</a><a href="#">Services</a><a href="#">Events</a><a href="#">Members</a><a href="#">Career</a><a href="#">Contact Us</a>
    </nav>
    <div class="abs header-rule"></div>
  </header>

  <section class="abs hero" role="img" aria-label="Combine harvester working a golden wheat field under a sunset sky">
    <div class="abs hero-copy">
      <h1>Welcome to our site</h1>
      <p>Consult us to improve<br>your agri business</p>
    </div>
    <div class="abs btn-join">Join Now
      <svg width="12" height="10" viewBox="0 0 12 10"><path d="M1 1l4 4-4 4M6 1l4 4-4 4" fill="none" stroke="#fff" stroke-width="1.3"/></svg>
    </div>
  </section>
  <div class="abs slider-dots"><span class="active"></span><span></span><span></span><span></span></div>

  <article class="abs feature" style="left:27px">
    <div class="feature-img" role="img" aria-label="Cupped hands holding a young tree" style="background:linear-gradient(135deg,#d8e6f0,#b9cfa0 60%,#8e9a70)"></div>
    <h2><em>Our</em> Services</h2>
    <p>Lorem ipsum dolor sit amet, consectetur adipisicing elit, sed do eiusmod tempor incididunt ut labore et dolore magna aliqua.</p>
    <div class="btn-more">More</div>
  </article>
  <article class="abs feature" style="left:319px">
    <div class="feature-img" role="img" aria-label="Scientist working with a pipette in a laboratory" style="background:linear-gradient(135deg,#5a6a78,#c9c2b4 55%,#e8e2d8)"></div>
    <h2><em>New</em> Technology</h2>
    <p>Lorem ipsum dolor sit amet, consectetur adipisicing elit, sed do eiusmod tempor incididunt ut labore et dolore magna aliqua.</p>
    <div class="btn-more">More</div>
  </article>
  <article class="abs feature" style="left:610px">
    <div class="feature-img" role="img" aria-label="Windmill on green farmland at sunset" style="background:linear-gradient(to bottom,#f0c878,#d8b070 50%,#6c7a34)"></div>
    <h2><em>Latest</em> Events</h2>
    <p>Lorem ipsum dolor sit amet, consectetur adipisicing elit, sed do eiusmod tempor incididunt ut labore et dolore magna aliqua.</p>
    <div class="btn-more">More</div>
  </article>

  <section class="abs about">
    <h2><em>About</em> Us</h2>
    <div class="about-rule"></div>
    <p>Lorem ipsum dolor sit amet, consectetur adipisicing elit, sed do eiusmod tempor incididunt ut labore et dolore magna aliqua. Ut enim ad minim veniam, quis nostrud exercitation ullamco laboris nisi ut aliquip ex ea commodo consequat. Duis aute irure dolor in reprehenderit in voluptate velit esse cillum dolore eu fugiat nulla pariatur. Excepteur sint occaecat cupidatat non proident, sunt in culpa qui officia deserunt mollit anim id est laborum.</p>
    <div class="btn-more">More</div>
  </section>

  <section class="abs subscribe">
    <h2><em>Subscribe</em> Us</h2>
    <div class="field">Your Name</div>
    <div class="field">Email id</div>
    <div class="btn-submit">Submit</div>
  </section>

  <footer class="abs footer">
    <nav class="footer-nav">
      <a class="current" href="#">Home</a><a href="#">About Us</a><a href="#">Services</a><a href="#">Events</a><a href="#">Members</a><a href="#">Career</a><a href="#">Contact Us</a>
    </nav>
    <div class="copyright">Copyright@2014, FenTrove</div>
  </footer>
</div>
</body>
</html>
```